Startup company business card (Media & Advertising)

we need a business card design for a company that is a startup in the media and aggregation industry. Card needs to look funky and of a new breed/modern and upmarket.

Target Market(s)

advertisers/ brand agencies & media publishers

Industry/Entity Type

Advertising

Contact Information for Business Card

Please ensure the front face signifies our brand (plumvexo.com) and back has details for the contact. Standard contact such as phone , address, email , website etc.

Font styles to use
Other font styles liked:
• use styleguide and logo font and color

Colors

Designer to choose colors to be used in the design.

Requirements
Must have
• We are disrupting the media and agency industry so subtlety would be good to use imagery to signify this
Nice to have
• Please use logo colors for branding
Should not have
• be as creative and provide few options. Pick a brand color from logo and styleguide

```html
<!DOCTYPE html>
<html lang="en">
<head>
<meta charset="utf-8">
<title>plumvexo business card</title>
<link href="https://fonts.googleapis.com/css2?family=Lato:wght@400;700;900&display=swap" rel="stylesheet">
<style>
  :root {
    --stage: #2b2623;
    --card: #0b0b0c;
    --card-edge: #161617;
    --brand-red: #e8344a;
    --brand-red-deep: #c61f3a;
    --ink-light: #f4f4f4;
    --divider: #6e2a2a;
    --pattern-a: #1a1a1b;
    --pattern-b: #0e0e0f;
  }
  * { box-sizing: border-box; margin: 0; padding: 0; }
  html, body { width: 1200px; height: 847px; overflow: hidden; }
  body {
    background: var(--stage);
    font-family: "Lato", sans-serif;
    position: relative;
  }
  .card {
    position: absolute;
    width: 520px;
    height: 298px;
    background: var(--card);
    border: 1px solid var(--card-edge);
    box-shadow: 0 14px 30px rgba(0,0,0,.45);
    overflow: hidden;
  }
  .card--front { left: 50px; top: 200px; }
  .card--back { left: 630px; top: 340px; }

  .front-pattern {
    position: absolute; inset: 0;
    background: radial-gradient(ellipse at 50% 45%, var(--pattern-a) 0%, var(--pattern-b) 75%);
  }
  .front-brand {
    position: absolute; left: 50%; top: 50%;
    transform: translate(-50%, -50%);
    display: flex; align-items: center; gap: 10px;
  }
  .brand-dot {
    width: 22px; height: 22px; border-radius: 50%;
    background: var(--brand-red);
  }
  .front-brand .brand-name { font-size: 24px; }
  .brand-name {
    font-weight: 700;
    color: var(--ink-light);
    letter-spacing: .5px;
  }

  .back-brand {
    position: absolute; left: 36px; top: 116px;
    display: flex; align-items: center; gap: 12px;
  }
  .back-brand .brand-name { font-size: 32px; }
  .divider {
    position: absolute; left: 246px; top: 56px;
    width: 1px; height: 186px;
    background: var(--divider);
  }
  .contact {
    position: absolute; left: 268px; top: 58px;
    color: var(--ink-light);
  }
  .contact__name {
    color: var(--brand-red);
    font-weight: 900;
    font-size: 24px;
    letter-spacing: .5px;
    text-transform: uppercase;
    line-height: 1.1;
  }
  .contact__title { font-size: 15px; margin-bottom: 10px; }
  .contact__address { font-size: 14px; line-height: 1.35; margin-bottom: 8px; }
  .contact__line {
    display: flex; align-items: center; gap: 9px;
    font-size: 14px; line-height: 1.55;
  }
  .contact__line svg { width: 13px; height: 13px; flex: none; }
  .contact__line--web { padding-left: 22px; }
  .accent { color: var(--brand-red); }
</style>
</head>
<body>
  <section class="card card--front" aria-label="Card front">
    <div class="front-pattern" role="img" aria-label="Tonal repeating brand pattern in dark greys"></div>
    <div class="front-brand">
      <span class="brand-dot"></span>
      <span class="brand-name">plumvexo</span>
    </div>
  </section>

  <section class="card card--back" aria-label="Card back">
    <div class="back-brand">
      <span class="brand-dot"></span>
      <span class="brand-name">plumvexo</span>
    </div>
    <div class="divider"></div>
    <div class="contact">
      <p class="contact__name">Dara Whitlow</p>
      <p class="contact__title">Founder &amp; CEO</p>
      <p class="contact__address">1234 First Line Address<br>5678 Second Line Address</p>
      <p class="contact__line">
        <svg viewBox="0 0 16 16" aria-hidden="true"><path fill="var(--brand-red)" d="M3.5 1.5l2.5 0 1 3.5-1.8 1.2a8 8 0 0 0 4.6 4.6L11 9l3.5 1v2.5c0 1-1 2-2 2A11 11 0 0 1 1.5 3.5c0-1 1-2 2-2z"/></svg>
        1234567890
      </p>
      <p class="contact__line">
        <svg viewBox="0 0 16 16" aria-hidden="true"><rect x="1" y="3" width="14" height="10" fill="var(--brand-red)"/><path d="M1 3l7 6 7-6" fill="none" stroke="var(--card)" stroke-width="1.3"/></svg>
        info@plumvexo.com
      </p>
      <p class="contact__line contact__line--web">www.<span class="accent">plumvexo</span>.com</p>
    </div>
  </section>
</body>
</html>
```